Restaurant, Nightclub

It's a Restaurant come nightclub. Our sign Lumen is white letters with blue edging on a black back ground.

Industry/Entity Type

Restaurant

Contact Information for Business Card

Lumen Stevenage Ltd
42 Mill Lane
Stevenage Herts SG2 7PQ

```html
<!DOCTYPE html>
<html lang="en">
<head>
<meta charset="utf-8">
<title>Lumen Stevenage Ltd – Business Card</title>
<link rel="stylesheet" href="https://fonts.googleapis.com/css2?family=Didact+Gothic&display=swap">
<style>
  :root {
    --brick-dark: #3a1d17;
    --brick-mid: #6b3326;
    --brick-warm: #80412f;
    --sign-black: #121214;
    --sign-edge: #26262a;
    --name-white: #ffffff;
    --tagline-blue: #6cc6ef;
    --contact-white: #ffffff;
  }
  html, body {
    margin: 0;
    padding: 0;
    width: 1200px;
    height: 792px;
    overflow: hidden;
    background: var(--brick-dark);
  }
  .card {
    position: relative;
    width: 1200px;
    height: 792px;
    overflow: hidden;
    font-family: "Didact Gothic", "Century Gothic", sans-serif;
  }
  .wall-photo {
    position: absolute;
    inset: 0;
    background:
      radial-gradient(ellipse at 70% 30%, var(--brick-warm) 0%, transparent 60%),
      linear-gradient(160deg, var(--brick-mid) 0%, var(--brick-dark) 55%, var(--brick-mid) 100%);
  }
  .sign-panel {
    position: absolute;
    left: 30px;
    top: 150px;
    width: 1140px;
    height: 330px;
    background: var(--sign-black);
    border: 2px solid var(--sign-edge);
    box-sizing: border-box;
  }
  .brand-name {
    position: absolute;
    left: 70px;
    top: 170px;
    margin: 0;
    font-size: 250px;
    font-weight: 400;
    line-height: 1;
    letter-spacing: 4px;
    color: var(--name-white);
  }
  .tagline {
    position: absolute;
    left: 450px;
    top: 500px;
    margin: 0;
    font-size: 62px;
    line-height: 1;
    color: var(--tagline-blue);
  }
  .contact {
    position: absolute;
    right: 43px;
    top: 585px;
    margin: 0;
    font-style: normal;
    font-size: 32px;
    line-height: 44px;
    text-align: right;
    color: var(--contact-white);
  }
</style>
</head>
<body>
  <main class="card">
    <div class="wall-photo" role="img" aria-label="Photograph of a red brick wall behind the illuminated sign"></div>
    <div class="sign-panel" aria-hidden="true"></div>
    <h1 class="brand-name">Lumen</h1>
    <p class="tagline">luxury restaurant/nightclub</p>
    <address class="contact">
      Lumen Stevenage Ltd<br>
      42 Mill Lane,<br>
      Stevenage Herts.<br>
      SG2 7PQ
    </address>
  </main>
</body>
</html>
```